Cover for "ROOTED! The skill and rhythm of guiding teams through calm and delight"

My first book for a global audience of modern performance leaders needs its cover!
I am an international executive coach and I've developed a new approach to replace classic Performance Management with a natural, sustainable approach fit for human beings :) My first book is about this approach and serves two purposes: helping leaders and sparking their curiosity to learn more, and positioning myself as a thought leader in the field.
The book is built on personal experience; it is both professional and personal ("From me to You"), and I'd like to position it beyond classic categorisation.
Its cover should communicate humanness, naturalness, ease and joy, within an unmistakably business-y context. I would like to see designs that use the color yellow (but not sure it communicates the right things).
Updates

Target Market(s)

Leaders who aspire to have a positive impact and deliver results in a meaningful way

Industry/Entity Type

Consulting & Executive Coaching - Trusted Advisor

Font styles to use
Other font styles liked:
• Helvetica Neue

Colors
0094D4
00A9DD
6FCCEA
C7EBF8
E9F6FB
FFC000
F8CF3A
FAE287
FDF2CF
FEFAEE
EE7325
F08F49
F5BC92
FAE3D3
FDF4ED

Requirements
Must have
• A both-and feeling to it (see description), e.g., masculine AND feminine, business AND humanness. Power with, not power over...
Should not have
• Too much "bling" - no classic status symbol business success language

```html
<!DOCTYPE html>
<html lang="en">
<head>
<meta charset="utf-8">
<title>ROOTED! – Book Cover</title>
<link rel="stylesheet" href="https://fonts.googleapis.com/css2?family=Roboto:ital,wght@0,700;1,700&display=swap">
<style>
  :root {
    --ink: #262626;
    --sun: #f2b900;
    --paper-top: #ffffff;
    --paper-bottom: #e2e2e2;
    --backdrop: #e6e6e6;
    --wood-light: #c9a24a;
    --wood-dark: #3a2415;
  }
  html, body {
    margin: 0;
    width: 1200px;
    height: 1200px;
    overflow: hidden;
    background: var(--backdrop);
  }
  .cover {
    position: absolute;
    left: 210px;
    top: 15px;
    width: 780px;
    height: 1170px;
  }
  .cover svg { display: block; }
  .title-letter {
    font-family: "Roboto", "Helvetica Neue", Arial, sans-serif;
    font-weight: 700;
    font-size: 190px;
    text-anchor: middle;
  }
  .subtitle {
    font-family: "Roboto", "Helvetica Neue", Arial, sans-serif;
    font-weight: 700;
    font-style: italic;
    font-size: 26px;
    fill: var(--sun);
  }
  .author {
    font-family: "Roboto", "Helvetica Neue", Arial, sans-serif;
    font-weight: 700;
    font-size: 44px;
    letter-spacing: 4px;
    fill: var(--ink);
  }
  .ink { fill: var(--ink); }
  .sun { fill: var(--sun); }
</style>
</head>
<body>
<div class="cover">
  <svg width="780" height="1170" viewBox="0 0 780 1170" xmlns="http://www.w3.org/2000/svg">
    <defs>
      <linearGradient id="paper" x1="0" y1="0" x2="0" y2="1">
        <stop offset="0.35" stop-color="var(--paper-top)"/>
        <stop offset="1" stop-color="var(--paper-bottom)"/>
      </linearGradient>
      <linearGradient id="piece-tone" x1="0" y1="0" x2="0" y2="1">
        <stop offset="0" stop-color="var(--wood-light)"/>
        <stop offset="0.35" stop-color="#6b4a2b"/>
        <stop offset="1" stop-color="var(--wood-dark)"/>
      </linearGradient>
      <clipPath id="upper-split"><polygon points="0,-200 780,-200 780,-139 0,836"/></clipPath>
      <clipPath id="lower-split"><polygon points="0,836 780,-139 780,1170 0,1170"/></clipPath>
      <clipPath id="above-accent"><polygon points="0,-200 780,-200 780,-54 0,987"/></clipPath>
      <clipPath id="below-accent"><polygon points="0,987 780,-54 780,1170 0,1170"/></clipPath>
    </defs>

    <rect class="cover-paper" width="780" height="1170" fill="url(#paper)"/>

    <!-- Title: staggered letters -->
    <g class="title">
      <g class="title-dark" clip-path="url(#upper-split)">
        <text class="title-letter ink" x="282" y="175">R</text>
        <text class="title-letter ink" x="500" y="257">O</text>
        <text class="title-letter ink" x="282" y="339">O</text>
        <text class="title-letter ink" x="500" y="421">T</text>
        <text class="title-letter ink" x="282" y="503">E</text>
        <text class="title-letter ink" x="500" y="585">D</text>
      </g>
      <g class="title-bright" clip-path="url(#lower-split)">
        <text class="title-letter sun" x="282" y="175">R</text>
        <text class="title-letter sun" x="500" y="257">O</text>
        <text class="title-letter sun" x="282" y="339">O</text>
        <text class="title-letter sun" x="500" y="421">T</text>
        <text class="title-letter sun" x="282" y="503">E</text>
        <text class="title-letter sun" x="500" y="585">D</text>
      </g>
      <text class="title-letter sun" x="282" y="667" clip-path="url(#above-accent)">!</text>
      <text class="title-letter ink" x="282" y="667" clip-path="url(#below-accent)">!</text>
    </g>

    <!-- Slash lines -->
    <g class="slash-dark">
      <line x1="460" y1="0" x2="150" y2="406" stroke="#ffffff" stroke-width="8"/>
      <line x1="460" y1="0" x2="150" y2="406" stroke="var(--ink)" stroke-width="1.6"/>
    </g>
    <g class="slash-bright">
      <line x1="420" y1="426" x2="180" y2="747" stroke="#ffffff" stroke-width="8"/>
      <line x1="420" y1="426" x2="180" y2="747" stroke="var(--sun)" stroke-width="1.6"/>
    </g>

    <!-- Subtitle band -->
    <g class="subtitle-band">
      <rect x="315" y="786" width="465" height="192" class="ink"/>
      <rect x="386" y="806" width="4" height="153" class="sun"/>
      <text class="subtitle" x="412" y="838">THE SKILL AND RHYTHM</text>
      <text class="subtitle" x="412" y="872">OF GUIDING TEAMS</text>
      <text class="subtitle" x="412" y="906">THROUGH CALM</text>
      <text class="subtitle" x="412" y="940">AND DELIGHT</text>
    </g>

    <!-- Chess piece placeholder -->
    <ellipse cx="283" cy="1033" rx="80" ry="8" fill="#b9b39a" opacity="0.6"/>
    <rect class="chess-piece" role="img" aria-label="Photo of a dark wooden chess pawn wearing a small gold crown"
          x="217" y="670" width="132" height="361" rx="40" fill="url(#piece-tone)"/>

    <!-- Author -->
    <text class="author" x="390" y="1130" text-anchor="middle">AUTHOR NAME</text>
  </svg>
</div>
</body>
</html>
```